Livestock Consulting Company has a logo but needs business cards and a uniform logo

My company works with farmers advising them on managing cattle and sheep. I have a logo but need business cards and a version of my logo to go onto my work shirts. I need the following wording added to my logo for my shirts "Tallowby Livestock Consulting".

```html
<!DOCTYPE html>
<html lang="en">
<head>
<meta charset="utf-8">
<title>Tallowby Livestock Consulting – Business Card</title>
<link rel="stylesheet" href="https://fonts.googleapis.com/css2?family=Saira:wght@700&family=Lato:wght@400&display=swap">
<style>
  :root {
    --brown: #7f6547;
    --white: #ffffff;
    --ink: #1d1d1d;
    --backdrop: #e6e6e4;
  }
  * { margin: 0; padding: 0; box-sizing: border-box; }
  html, body { width: 1200px; height: 1007px; overflow: hidden; }
  body {
    background: var(--backdrop);
    position: relative;
    font-family: "Lato", sans-serif;
  }
  .card {
    position: absolute;
    left: 280px;
    width: 640px;
    height: 366px;
    overflow: hidden;
    box-shadow: 0 6px 18px rgba(0,0,0,0.18);
  }
  .card--front { top: 96px; background: var(--brown); }
  .card--back { top: 545px; background: var(--white); }

  .wordmark {
    font-family: "Saira", sans-serif;
    font-weight: 700;
    text-transform: uppercase;
    display: flex;
    align-items: center;
    gap: 14px;
  }
  .wordmark__dot {
    width: 22px; height: 22px; border-radius: 50%;
    flex: none;
  }
  .wordmark__text { line-height: 1; }
  .wordmark__line1 { display: block; font-size: 38px; letter-spacing: 1px; }
  .wordmark__line2 { display: block; font-size: 18px; letter-spacing: 9px; margin-top: 6px; text-align: center; }

  .card--front .wordmark {
    position: absolute; left: 0; right: 0; top: 140px;
    justify-content: center; color: var(--white);
  }
  .card--front .wordmark__dot { background: var(--white); }

  .card--back .wordmark {
    position: absolute; right: 70px; top: 48px;
    color: var(--brown);
  }
  .card--back .wordmark__line1 { font-size: 30px; }
  .card--back .wordmark__line2 { font-size: 14px; letter-spacing: 7px; }
  .card--back .wordmark__dot { background: var(--brown); width: 18px; height: 18px; }

  .band {
    position: absolute; left: 0; right: 0; top: 160px; height: 146px;
    background: var(--brown);
    display: flex; align-items: center; justify-content: center;
    color: var(--white);
  }
  .person { text-align: right; padding-right: 22px; }
  .person__name {
    font-family: "Saira", sans-serif; font-weight: 700;
    font-size: 26px; letter-spacing: 1px; text-transform: uppercase;
  }
  .person__role { font-size: 20px; margin-top: 2px; }
  .divider { width: 2px; height: 84px; background: var(--white); }
  .contacts { list-style: none; padding-left: 22px; font-size: 17px; line-height: 1.55; }
  .contacts li { display: flex; align-items: center; gap: 8px; }
  .contacts svg { width: 14px; height: 14px; flex: none; fill: var(--white); }

  .address {
    position: absolute; left: 0; right: 0; top: 318px;
    text-align: center; font-size: 19px; color: var(--ink);
  }
</style>
</head>
<body>
  <section class="card card--front" aria-label="Card front">
    <div class="wordmark">
      <span class="wordmark__dot"></span>
      <span class="wordmark__text">
        <span class="wordmark__line1">Tallowby Livestock</span>
        <span class="wordmark__line2">Consulting</span>
      </span>
    </div>
  </section>

  <section class="card card--back" aria-label="Card back">
    <div class="wordmark">
      <span class="wordmark__dot"></span>
      <span class="wordmark__text">
        <span class="wordmark__line1">Tallowby Livestock</span>
        <span class="wordmark__line2">Consulting</span>
      </span>
    </div>

    <div class="band">
      <div class="person">
        <p class="person__name">Daniel Tallowby</p>
        <p class="person__role">Director</p>
      </div>
      <div class="divider"></div>
      <ul class="contacts">
        <li>
          <svg viewBox="0 0 16 16" aria-hidden="true"><path d="M3 1h3l1.5 4-2 1.5a9 9 0 0 0 4 4L11 8.5l4 1.5v3a2 2 0 0 1-2 2A12 12 0 0 1 1 3a2 2 0 0 1 2-2z"/></svg>
          (555) 014-2278
        </li>
        <li>
          <svg viewBox="0 0 16 16" aria-hidden="true"><path d="M1 3h14v10H1z M2 4l6 5 6-5" fill="none" stroke="#fff" stroke-width="1.4"/></svg>
          info@tallowbylivestock.com
        </li>
        <li>
          <svg viewBox="0 0 16 16" aria-hidden="true"><circle cx="8" cy="8" r="7"/></svg>
          www.tallowbylivestock.com
        </li>
      </ul>
    </div>

    <p class="address">412 Millbrook Road Suite 20C Ashford NY 10544</p>
  </section>
</body>
</html>
```